Luminously Grounded Vitality

We want to design a business card that is modern and appealing for an innovative psychedelic telemedicine company that provides at-home ketamine-assisted therapy along with wellness, longevity, and anti-aging medicines. We want to use our deep purple and white plus other colors you can find on our website. We don't have any strict brand guidelines yet so feel free to get creative. We want a very professional, but technology first modern design that will instill trust, peace, calm, but also be attractive to investors in the healthcare and SaaS space.

```html
<!DOCTYPE html>
<html lang="en">
<head>
<meta charset="utf-8">
<title>Luminously Grounded Vitality – Business Card</title>
<link href="https://fonts.googleapis.com/css2?family=Montserrat:wght@400;500;700&family=Tenor+Sans&display=swap" rel="stylesheet">
<style>
  :root {
    --deep-purple: #28143f;
    --deep-purple-soft: #362253;
    --lavender: #7b63ad;
    --lavender-light: #9b88c4;
    --ink: #1c1c1c;
    --paper: #f7f7f7;
    --mist: #d9d7dc;
    --backdrop: #e9e7ec;
  }
  * { box-sizing: border-box; margin: 0; padding: 0; }
  html, body {
    width: 1200px; height: 900px; overflow: hidden;
    background: var(--backdrop);
  }
  .canvas { position: relative; width: 1200px; height: 900px; }
  .card {
    position: absolute; width: 700px; height: 400px;
    overflow: hidden; border-radius: 4px;
    box-shadow: 0 10px 30px rgba(40, 20, 63, 0.18);
  }

  /* Contact side */
  .card-contact { left: 60px; top: 60px; background: var(--paper); font-family: "Montserrat", sans-serif; color: var(--ink); }
  .accent-band { position: absolute; left: 420px; right: 0; top: 92px; height: 20px; background: var(--lavender); }
  .brand-label {
    position: absolute; left: 310px; top: 112px;
    background: var(--lavender); color: #fff;
    font-weight: 700; font-size: 17px; letter-spacing: 0.5px;
    padding: 3px 14px 4px 18px;
  }
  .tagline { position: absolute; left: 330px; top: 146px; font-size: 22px; font-weight: 700; }
  .role { position: absolute; left: 332px; top: 178px; font-size: 15px; font-weight: 500; }
  .contact-list { position: absolute; left: 332px; top: 212px; list-style: none; font-size: 14.5px; font-weight: 500; }
  .contact-list li { display: flex; align-items: flex-start; gap: 10px; margin-bottom: 9px; line-height: 1.3; }
  .contact-list svg { flex: none; margin-top: 2px; }
  .brand-mark { position: absolute; left: 60px; top: 150px; width: 200px; text-align: center; }
  .brand-mark .dot { width: 120px; height: 120px; border-radius: 50%; background: var(--lavender); margin: 0 auto 16px; }
  .brand-mark .name { color: var(--lavender); font-weight: 700; font-size: 15px; line-height: 1.3; }

  /* Brand side */
  .card-brand { left: 440px; top: 440px; background: var(--deep-purple); font-family: "Tenor Sans", sans-serif; }
  .backdrop-circle { position: absolute; right: -90px; top: 40px; width: 420px; height: 420px; border-radius: 50%; background: var(--deep-purple-soft); }
  .brand-lockup { position: absolute; left: 50px; top: 160px; display: flex; align-items: center; gap: 22px; }
  .brand-lockup .dot { width: 70px; height: 70px; border-radius: 50%; background: var(--mist); flex: none; }
  .brand-lockup .name { color: #fff; font-size: 36px; line-height: 1.1; }
</style>
</head>
<body>
<main class="canvas">
  <section class="card card-contact" aria-label="Contact side">
    <div class="accent-band"></div>
    <div class="brand-label">Luminously Grounded Vitality</div>
    <p class="tagline">Mental health service</p>
    <p class="role">Co-funder name</p>
    <ul class="contact-list">
      <li>
        <svg width="16" height="16" viewBox="0 0 16 16"><circle cx="8" cy="8" r="8" fill="var(--lavender)"/><path d="M5.2 4.2l1.6-.4.8 1.9-1 .7c.4.9 1.1 1.6 2 2l.7-1 1.9.8-.4 1.6c-3 .2-5.8-2.6-5.6-5.6z" fill="#fff"/></svg>
        <span>555-014-2290</span>
      </li>
      <li>
        <svg width="16" height="16" viewBox="0 0 16 16"><circle cx="8" cy="8" r="8" fill="var(--lavender)"/><circle cx="8" cy="8" r="4.5" fill="none" stroke="#fff" stroke-width="1"/><path d="M3.5 8h9M8 3.5c-2 2.4-2 6.6 0 9M8 3.5c2 2.4 2 6.6 0 9" fill="none" stroke="#fff" stroke-width="0.9"/></svg>
        <span>www.luminouslygrounded.com</span>
      </li>
      <li>
        <svg width="16" height="18" viewBox="0 0 16 18"><path d="M8 0a6 6 0 0 1 6 6c0 4.5-6 12-6 12S2 10.5 2 6a6 6 0 0 1 6-6z" fill="var(--lavender)"/><circle cx="8" cy="6" r="2.2" fill="#fff"/></svg>
        <span>2750 Aurora Lane, Suite 300,<br>Boulder, CO, United States, Colorado</span>
      </li>
    </ul>
    <div class="brand-mark">
      <div class="dot"></div>
      <p class="name">Luminously Grounded Vitality</p>
    </div>
  </section>

  <section class="card card-brand" aria-label="Brand side">
    <div class="backdrop-circle"></div>
    <div class="brand-lockup">
      <div class="dot"></div>
      <p class="name">Luminously Grounded<br>Vitality</p>
    </div>
  </section>
</main>
</body>
</html>
```